Fish Farm needing 3 - Fold Flyer / Price List designed

We are looking for a new Price List for our Fish Farm. I have attached an example of the basic info that needs in the flyer. We want the flyer to be a 3 fold page. Anything that is on our website, you can use for ideas. There are some pictures on there that can be photoshopped into the flyer. Do not use any photos from any other sites. We are looking for something professional but fun and exciting! I have also attached our business logo. We tend to stay with the blues and greens for colors. Let's get started....
Updates

Need extra days to review

Contact Information for Business Card

We are needing a business card with our new logo on it. We also need our address, phone numbers, email address, and website listed. Please view our website for more ideas.

Colors

Designer to choose colors to be used in the design.

```html
<!DOCTYPE html>
<html lang="en">
<head>
<meta charset="utf-8">
<title>Marlow's Fish Farm – 2019 Price List Tri-Fold</title>
<link rel="stylesheet" href="https://fonts.googleapis.com/css2?family=Roboto:wght@300;400;700&family=Tinos:wght@400;700&family=Alex+Brush&display=swap">
<style>
:root{
  --page:#3b3b3d;
  --deep:#0d2f86;
  --ocean:#1565c0;
  --ocean-mid:#1d72c6;
  --ocean-light:#2e86d6;
  --brand:#1f3fa8;
  --navy:#1a237e;
  --white:#ffffff;
  --mist:#e9ecf1;
  --rule:rgba(255,255,255,.75);
}
*{box-sizing:border-box;margin:0;padding:0}
html,body{width:1200px;height:1200px;overflow:hidden;background:var(--page)}
body{position:relative;font-family:'Roboto',Arial,sans-serif;color:var(--white)}
.sheet{position:absolute;left:260px;width:681px;height:528px;overflow:hidden;
  background:linear-gradient(180deg,var(--ocean-light) 0%,var(--ocean) 55%,#1858ad 100%);
  box-shadow:0 14px 28px rgba(0,0,0,.45)}
.sheet--outside{top:29px}
.sheet--inside{top:621px;background:linear-gradient(180deg,#1b63b8 0%,#2270c2 50%,#1a5fb3 100%)}
.shapes{position:absolute;inset:0}
.abs{position:absolute}
.serif{font-family:'Tinos','Times New Roman',serif;font-weight:700}
.map,.photo{position:absolute}
.map{left:15px;top:0;width:201px;height:269px;background:linear-gradient(135deg,#fafafa,#e4e4e4)}
.photo{left:224px;top:0;width:200px;height:370px;background:linear-gradient(160deg,#1a52b8 0%,#1f73cf 45%,#2a4f9c 100%)}
.small{font-size:7.4px;line-height:10px}
.note-rule{height:1px;background:var(--rule);margin:6px 0}
.wordmark{font-weight:700;font-family:'Roboto',Arial,sans-serif;letter-spacing:.3px;text-align:center;line-height:1}
.ticks{list-style:none;font-size:9.2px;line-height:15.3px}
.ticks li{display:flex;align-items:center;gap:7px}
.ticks svg{width:7px;height:7px}
.contact{text-align:center;color:#222;font-size:7.6px;line-height:12px}
.contact b{color:var(--brand);font-style:italic}
.contact .llc{font-family:'Roboto',Arial,sans-serif;font-weight:700;font-size:20px;line-height:24px;color:var(--brand)}
.contact .row{display:flex;align-items:center;justify-content:center;gap:3px}
.contact svg{width:8px;height:8px}
.head{font-family:'Tinos','Times New Roman',serif;font-weight:700;font-size:11.2px;line-height:13px;letter-spacing:.3px}
.tbl{display:flex;font-size:7.8px;line-height:10.4px;margin-top:6px}
.tbl .col{padding:0 8px 2px 8px;border-left:1px solid var(--rule)}
.tbl .col:first-child{border-left:0;padding-left:0}
.tbl .th{font-family:'Tinos','Times New Roman',serif;font-weight:700;font-size:9px;line-height:13px}
.script{font-family:'Alex Brush',cursive;font-size:50px;line-height:1}
</style>
</head>
<body>

<!-- Outside of the tri-fold -->
<section class="sheet sheet--outside">
  <svg class="shapes" viewBox="0 0 681 528" preserveAspectRatio="none">
    <defs>
      <linearGradient id="gDeep" x1="0" y1="0" x2="1" y2="1">
        <stop offset="0" stop-color="#0d2f86"/><stop offset="1" stop-color="#1b4fb0"/>
      </linearGradient>
      <linearGradient id="gMist" x1="0" y1="0" x2="1" y2="0">
        <stop offset="0" stop-color="#c9ced6"/><stop offset="1" stop-color="#f4f5f7"/>
      </linearGradient>
    </defs>
    <rect x="412" y="0" width="40" height="528" fill="url(#gMist)"/>
    <path d="M0 0 H412 C440 90 440 220 360 300 C280 380 150 400 0 335 Z" fill="url(#gDeep)"/>
    <path d="M412 0 C440 90 440 220 360 300 C280 380 150 400 0 335" fill="none" stroke="#fff" stroke-width="6"/>
    <path d="M395 340 C420 380 445 440 450 528 H390 C400 460 400 400 395 340Z" fill="url(#gMist)" opacity=".9"/>
    <rect x="450" y="0" width="231" height="528" fill="#fff"/>
    <path d="M681 75 C600 85 475 120 455 230 L450 420 C520 400 600 382 681 378 Z" fill="#1a6fc9"/>
    <path d="M450 420 C520 400 600 382 681 378" fill="none" stroke="#23318f" stroke-width="3"/>
  </svg>

  <div class="map" role="img" aria-label="Hand-drawn road map showing the route to the farm"></div>

  <div class="abs small" style="left:18px;top:276px;width:196px">
    Feel free to call the farm or the cell phone. If no answer, leave a message and we will get back to you as soon as possible.
    <div class="note-rule"></div>
    Always call before coming to the farm as we may be on a delivery.
  </div>

  <div class="abs" style="left:0;top:430px;width:223px;text-align:center;font-weight:300;font-size:15px;line-height:20px">
    Our Sales Route Schedule is listed on our website at:
  </div>
  <div class="abs" style="left:0;top:478px;width:223px;text-align:center;font-size:7.6px">www.marlowsfishfarm.com/schedule</div>

  <div class="photo" role="img" aria-label="Underwater photo of colourful tropical fish over coral"
       style="clip-path:path('M0 0 H188 C205 90 205 220 136 300 C100 340 40 365 0 378 Z')"></div>
  <div class="abs wordmark" style="left:258px;top:44px;width:132px;font-size:15px;color:#fff">MARLOW'S FISH FARM</div>

  <div class="abs serif" style="left:230px;top:403px;font-size:13.6px;line-height:18px;letter-spacing:.3px">STANDARD<br>STOCKING RATES</div>
  <div class="abs" style="left:229px;top:440px;font-size:15px">Per Surface Acre</div>
  <div class="abs small" style="left:230px;top:458px;line-height:11.8px">
    600-1,000 Hybrid Bluegill, Regular<br>Bluegill, or Redear<br>100-200 Largemouth Bass<br>100-200 Channel Catfish<br>3,000-5,000 Fathead Minnows
  </div>

  <div class="abs wordmark" style="left:476px;top:30px;width:180px;font-size:22px;color:var(--brand)">MARLOW'S FISH FARM</div>

  <div class="abs" style="left:455px;top:100px;width:226px;display:flex;align-items:center;justify-content:center;gap:5px">
    <span style="width:22px;height:2px;background:#fff"></span>
    <span style="font-family:'Tinos',serif;font-size:48px;line-height:50px">2019</span>
    <span style="width:22px;height:2px;background:#fff"></span>
  </div>
  <div class="abs" style="left:455px;top:148px;width:226px;text-align:center;font-family:'Tinos',serif;font-size:18.5px">PRICE LIST FOR:</div>
  <ul class="abs ticks" style="left:518px;top:182px">
    <li><svg viewBox="0 0 10 10"><circle cx="5" cy="5" r="5" fill="#fff"/><path d="M2.6 5.2 L4.4 7 L7.6 3.4" stroke="#1a6fc9" stroke-width="1.5" fill="none"/></svg>HYBRID BLUEGILL</li>
    <li><svg viewBox="0 0 10 10"><circle cx="5" cy="5" r="5" fill="#fff"/><path d="M2.6 5.2 L4.4 7 L7.6 3.4" stroke="#1a6fc9" stroke-width="1.5" fill="none"/></svg>REGULAR BLUEGILL</li>
    <li><svg viewBox="0 0 10 10"><circle cx="5" cy="5" r="5" fill="#fff"/><path d="M2.6 5.2 L4.4 7 L7.6 3.4" stroke="#1a6fc9" stroke-width="1.5" fill="none"/></svg>REDEAR SUNFISH</li>
    <li><svg viewBox="0 0 10 10"><circle cx="5" cy="5" r="5" fill="#fff"/><path d="M2.6 5.2 L4.4 7 L7.6 3.4" stroke="#1a6fc9" stroke-width="1.5" fill="none"/></svg>LARGEMOUTH BASS</li>
    <li><svg viewBox="0 0 10 10"><circle cx="5" cy="5" r="5" fill="#fff"/><path d="M2.6 5.2 L4.4 7 L7.6 3.4" stroke="#1a6fc9" stroke-width="1.5" fill="none"/></svg>FATHEAD MINNOWS</li>
    <li><svg viewBox="0 0 10 10"><circle cx="5" cy="5" r="5" fill="#fff"/><path d="M2.6 5.2 L4.4 7 L7.6 3.4" stroke="#1a6fc9" stroke-width="1.5" fill="none"/></svg>GOLDEN SHINERS</li>
    <li><svg viewBox="0 0 10 10"><circle cx="5" cy="5" r="5" fill="#fff"/><path d="M2.6 5.2 L4.4 7 L7.6 3.4" stroke="#1a6fc9" stroke-width="1.5" fill="none"/></svg>TRIPLOID GRASS CARP</li>
    <li><svg viewBox="0 0 10 10"><circle cx="5" cy="5" r="5" fill="#fff"/><path d="M2.6 5.2 L4.4 7 L7.6 3.4" stroke="#1a6fc9" stroke-width="1.5" fill="none"/></svg>CHANNEL CATFISH</li>
    <li><svg viewBox="0 0 10 10"><circle cx="5" cy="5" r="5" fill="#fff"/><path d="M2.6 5.2 L4.4 7 L7.6 3.4" stroke="#1a6fc9" stroke-width="1.5" fill="none"/></svg>ALBINO CATFISH</li>
    <li><svg viewBox="0 0 10 10"><circle cx="5" cy="5" r="5" fill="#fff"/><path d="M2.6 5.2 L4.4 7 L7.6 3.4" stroke="#1a6fc9" stroke-width="1.5" fill="none"/></svg>BLACK CRAPPIE</li>
    <li><svg viewBox="0 0 10 10"><circle cx="5" cy="5" r="5" fill="#fff"/><path d="M2.6 5.2 L4.4 7 L7.6 3.4" stroke="#1a6fc9" stroke-width="1.5" fill="none"/></svg>JAPANESE KOI</li>
    <li><svg viewBox="0 0 10 10"><circle cx="5" cy="5" r="5" fill="#fff"/><path d="M2.6 5.2 L4.4 7 L7.6 3.4" stroke="#1a6fc9" stroke-width="1.5" fill="none"/></svg>TILAPIA</li>
  </ul>

  <div class="abs contact" style="left:452px;top:392px;width:229px">
    <div class="llc">MARLOW'S<br>FISH FARM, LLC</div>
    <div><b>Farm:</b> <i>(555) 214-0187</i></div>
    <div><b>Cell:</b> <i>(555) 630-2291</i></div>
    <div><b>Text:</b> <i>(555) 613-4470</i></div>
    <div class="row"><svg viewBox="0 0 10 10"><circle cx="5" cy="5" r="4.2" fill="none" stroke="#23318f" stroke-width="1.4"/><circle cx="5" cy="4.5" r="1.5" fill="#23318f"/></svg>4810 E. Willow Creek Rd. Fairhaven, IN 47000</div>
    <div class="row"><svg viewBox="0 0 10 10"><rect x="1" y="2.5" width="8" height="5.5" rx="1" fill="#23318f"/></svg>marlowsfishfarm@mailpond.net</div>
    <div class="row"><svg viewBox="0 0 10 10"><circle cx="5" cy="5" r="4.2" fill="none" stroke="#23318f" stroke-width="1.4"/></svg>www.marlowsfishfarm.com</div>
  </div>
</section>

<!-- Inside of the tri-fold -->
<section class="sheet sheet--inside">
  <svg class="shapes" viewBox="0 0 681 528" preserveAspectRatio="none">
    <rect x="223" y="0" width="1" height="528" fill="rgba(255,255,255,.12)"/>
    <rect x="448" y="0" width="1" height="528" fill="rgba(255,255,255,.12)"/>
    <path d="M316 528 C340 430 400 392 450 380 C545 360 625 335 681 290 V528 Z" fill="#eef0f4"/>
    <path d="M316 528 C340 430 400 392 450 380 C545 360 625 335 681 290" fill="none" stroke="#23318f" stroke-width="3"/>
    <rect x="18" y="453" width="185" height="1" fill="rgba(255,255,255,.8)"/>
  </svg>

  <div class="abs script" style="left:16px;top:18px">Price List</div>

  <div class="abs" style="left:14px;top:90px">
    <div class="head">HYBRID BLUEGILL<br>(HYBRID SUNFISH)</div>
    <div class="tbl" style="margin-left:4px">
      <div class="col"><div class="th">Size</div>1-3 Inch<br>3-5 Inch<br>*5-7 Inch</div>
      <div class="col"><div class="th">Each</div>50¢<br>80¢<br>$1.75</div>
      <div class="col" style="padding-right:42px"><div class="th">1000</div>45¢<br>75¢</div>
      <div class="col" style="padding-bottom:16px"><div class="th">3000</div>40¢</div>
    </div>
  </div>

  <div class="abs" style="left:18px;top:199px">
    <div class="head">REGULAR BLUEGILL</div>
    <div class="tbl">
      <div class="col"><div class="th">Size</div>1-3 Inch<br>3-5 Inch</div>
      <div class="col"><div class="th">Each</div>50¢<br>80¢</div>
      <div class="col"><div class="th">1000</div>45¢<br>75¢</div>
    </div>
  </div>

  <div class="abs" style="left:18px;top:281px">
    <div class="head">REDEAR SUNFISH</div>
    <div class="tbl">
      <div class="col"><div class="th">Size</div>1-3 Inch<br>3-4 Inch<br>*4-5 Inch</div>
      <div class="col"><div class="th">Each</div>50¢<br>75¢<br>$1.00</div>
      <div class="col"><div class="th">1000</div>45¢<br>70¢<br>95¢</div>
    </div>
  </div>

  <div class="abs" style="left:18px;top:368px">
    <div class="head">LARGEMOUTH BASS</div>
    <div class="tbl">
      <div class="col"><div class="th">Size</div>1-3 Inch<br>3-4 Inch<br>*4-6 Inch<br>*6-8 Inch</div>
      <div class="col"><div class="th">Each</div>$1.10<br>$1.20<br>$1.95<br>$2.75</div>
    </div>
  </div>

  <div class="abs" style="left:20px;top:462px;font-style:italic;font-size:11px;line-height:14.5px">*When Available.<br>Sizes Vary Depending on<br>Time of Year</div>

  <div class="abs" style="left:244px;top:12px">
    <div class="head">TRIPLOID&nbsp; GRASS CARP<br>(Indiana Prices)</div>
    <div class="tbl" style="margin-top:10px">
      <div class="col" style="padding-right:12px">8-11 Inch<br>5-24 Grass Carp<br>25-49 Grass Carp<br>50-99 Grass Carp<br>100+ Grass Carp</div>
      <div class="col">Minimum 5<br>$16.00 each<br>$15.00 each<br>$14.00 each<br>Inquire</div>
    </div>
  </div>

  <div class="abs" style="left:243px;top:123px">
    <div class="head">CHANNEL CATFISH</div>
    <div class="tbl">
      <div class="col" style="padding-right:18px"><div class="th">Size</div>6-8 Inch</div>
      <div class="col" style="padding-right:38px"><div class="th">Each</div>65¢</div>
      <div class="col"><div class="th">1000</div>60¢</div>
    </div>
  </div>

  <div class="abs" style="left:243px;top:190px">
    <div class="head">ALBINO CATFISH (March &amp; April)</div>
    <div class="tbl">
      <div class="col" style="padding-right:18px"><div class="th">Size</div>5-8 Inch</div>
      <div class="col"><div class="th">Each</div>$1.20</div>
    </div>
  </div>

  <div class="abs" style="left:243px;top:255px">
    <div class="head">BLACK CRAPPIE (March &amp; April)</div>
    <div class="tbl">
      <div class="col" style="padding-right:18px"><div class="th">Size</div>3-5 Inch</div>
      <div class="col"><div class="th">Each</div>$1.10</div>
    </div>
  </div>

  <div class="abs" style="left:243px;top:317px">
    <div class="head">FATHEAD MINNOWS</div>
    <div class="small" style="margin-top:6px">$36.00 per thousand<br>($9.00 per lb.)</div>
  </div>

  <div class="abs" style="left:242px;top:376px">
    <div class="head">FATHEAD MINNOWS</div>
    <div class="small" style="margin-top:5px">(Delivery Only – Minimum 50 lb.)</div>
    <div class="small" style="display:flex;gap:44px"><span>50-99 lb<br>100+ lb</span><span>$8.00 lb<br>$7.50 lb.</span></div>
  </div>

  <div class="abs" style="left:465px;top:13px">
    <div class="head">FLOATING FISH FOOD</div>
    <div class="small" style="margin-top:4px">Starter Size (50 lb. Bag)<br>41% Protein<br>Market Price – Inquire<br>(Only Available at Farm)</div>
  </div>

  <div class="abs" style="left:464px;top:90px">
    <div class="head">TILAPIA&nbsp; (May 15 – June 30)</div>
    <div class="small" style="margin-top:8px">5-10 Tilapia per lb.</div>
    <div class="small" style="display:flex;gap:40px;margin-top:5px;line-height:11.2px"><span>1-25 lb.<br>26-40 lb.<br>40-50 lb.<br>50+ lb</span><span>$15.00 lb.<br>$14.00 lb.<br>$13.00 lb.<br>$12.00 lb.</span></div>
  </div>

  <div class="abs" style="left:465px;top:189px">
    <div class="head">JAPANESE KOI</div>
    <div class="tbl" style="margin-top:4px">
      <div class="col" style="padding-right:30px"><div class="th">Size</div>4-5 Inch<br>6-8 Inch<br>*9-12 Inch</div>
      <div class="col"><div class="th">Each</div>$6.00<br>$10.00<br>$15.00</div>
    </div>
  </div>

  <div class="abs head" style="left:464px;top:277px">BUTTERFLY KOI<br>ALSO AVAILABLE!</div>
  <div class="abs head" style="left:464px;top:314px">PRICES SUBJECT TO CHANGE<br>WITHOUT NOTICE</div>

  <div class="abs contact" style="left:450px;top:384px;width:231px">
    <div class="llc">MARLOW'S<br>FISH FARM, LLC</div>
    <div><b>Farm:</b> <i>(555) 214-0187</i></div>
    <div><b>Cell:</b> <i>(555) 630-2291</i></div>
    <div><b>Text:</b> <i>(555) 613-4470</i></div>
    <div class="row"><svg viewBox="0 0 10 10"><circle cx="5" cy="5" r="4.2" fill="none" stroke="#23318f" stroke-width="1.4"/><circle cx="5" cy="4.5" r="1.5" fill="#23318f"/></svg>4810 E. Willow Creek Rd. Fairhaven, IN 47000</div>
    <div class="row"><svg viewBox="0 0 10 10"><rect x="1" y="2.5" width="8" height="5.5" rx="1" fill="#23318f"/></svg>marlowsfishfarm@mailpond.net</div>
    <div class="row"><svg viewBox="0 0 10 10"><circle cx="5" cy="5" r="4.2" fill="none" stroke="#23318f" stroke-width="1.4"/></svg>www.marlowsfishfarm.com</div>
  </div>
</section>

</body>
</html>
```